Business Card For Video Production Company

Please NOTE: I've added some info to the must haves that I should have included at the start. Thank you.

I need a business card design for my video production company based in Orlando called Caldera Film Works. Our work consists of web video marketing (web videos), training videos, sales videos, conference and seminar video production...basically a lot of corporate based work.

We work with successful small businesses, not-for-profits and some Fortune 500 type groups. We bring a lot of knowledge, experience and attention to detail to every project.

I'd like something that communicates strength, confidence, integrity, as well as creative vision. I want to stay away from the standard icons of the media and film industry. I'd like to emphasize the colors of my logo, and also the colors of my website which has a white background. Simple is good.

Our budgets are moderate...generally $1500 to $5000.

www.calderafilm.tv

PS...We don't do weddings or recitals, or that type of production.
Updates

I want to thank all the designers for your updates. There's way too many to be able to give feedback on for all. I hope you understand that. But wow…there are so many great designs everyone has offered. I can't thank you enough…each and everyone. I hope to make my decision soon. I'm not accepting anymore designs from new designers. Brent-

Target Market(s)

Successful small businesses, marketing directors, corporate communication directors, training and human resources professionals. forward thinking not-for profits. Since my company is based in Central Florida, most of my work comes from this area too.

Industry/Entity Type

Marketing

Requirements
Must have
• website address, www.calderafilm.tv
phone number, 407-552-9031
email address, brent@calderafilm.tv

Title
Brent Caldera
Owner/Creative Director

I'd like to have a single line that goes across illustrating our services, maybe separated with bullet points:

Marketing Videos, Corporate Videos, Conference & Seminar Video Production
Should not have
• No film or video icons.
No need to pull language or copy from my website.

```html
<!DOCTYPE html>
<html lang="en">
<head>
<meta charset="utf-8">
<title>Caldera Film Works – Business Card</title>
<link href="https://fonts.googleapis.com/css2?family=Montserrat:wght@700&family=Arimo:wght@400&display=swap" rel="stylesheet">
<style>
  :root {
    --page: #2b2b2d;
    --card: #ffffff;
    --ink: #4a4a4c;
    --ink-soft: #5c5c5e;
    --blue: #0a8fd6;
    --sky: #8ed6f5;
    --bar-grey: #4d4d4f;
  }
  * { box-sizing: border-box; margin: 0; padding: 0; }
  html, body {
    width: 1200px; height: 900px; overflow: hidden;
    background: var(--page);
    font-family: "Arimo", Arial, sans-serif;
  }
  .card {
    position: absolute;
    width: 700px; height: 400px;
    background: var(--card);
    box-shadow: 0 14px 30px rgba(0,0,0,.45);
    overflow: hidden;
  }
  .card--front { left: 250px; top: 40px; }
  .card--back  { left: 250px; top: 470px; }

  .brand {
    position: absolute; left: 60px; top: 128px;
    display: flex; align-items: center; gap: 14px;
  }
  .brand__mark { width: 30px; height: 30px; background: var(--blue); }
  .brand__name {
    font-family: "Montserrat", Arial, sans-serif; font-weight: 700;
    font-size: 34px; color: var(--ink); letter-spacing: -0.5px;
  }

  .person { position: absolute; right: 40px; top: 26px; text-align: right; }
  .person__name {
    font-family: "Montserrat", Arial, sans-serif; font-weight: 700;
    font-size: 22px; color: var(--ink);
  }
  .person__title { font-size: 15px; color: var(--ink-soft); margin-top: 2px; }

  .services {
    position: absolute; right: 40px; top: 150px;
    list-style: none; text-align: right;
    font-size: 16px; line-height: 22px; color: var(--ink-soft);
  }

  .contact {
    position: absolute; left: 60px; bottom: 60px;
    list-style: none; font-size: 18px; color: var(--ink);
  }
  .contact__item { display: flex; align-items: center; gap: 12px; height: 30px; }
  .contact__icon { width: 20px; height: 20px; flex: none; }

  .band { position: absolute; bottom: 0; }
  .band--grey { left: 0; width: 430px; height: 22px; background: var(--bar-grey); }
  .band--blue { left: 438px; width: 170px; height: 30px; background: var(--blue); }
  .band--sky  { left: 616px; width: 84px; height: 30px; background: var(--sky); }

  .back-brand {
    position: absolute; inset: 0;
    display: flex; align-items: center; justify-content: center; gap: 20px;
  }
  .back-brand__mark { width: 44px; height: 44px; background: var(--sky); }
  .back-brand__name {
    font-family: "Montserrat", Arial, sans-serif; font-weight: 700;
    font-size: 46px; color: var(--blue); letter-spacing: -0.5px;
  }
</style>
</head>
<body>

<section class="card card--front">
  <div class="brand">
    <span class="brand__mark"></span>
    <span class="brand__name">Caldera Film Works</span>
  </div>

  <div class="person">
    <p class="person__name">Brent Caldera</p>
    <p class="person__title">Owner/Creative Director</p>
  </div>

  <ul class="services">
    <li>Marketing Videos</li>
    <li>Corporate Videos</li>
    <li>Conference &amp; Seminar Video Production</li>
  </ul>

  <ul class="contact">
    <li class="contact__item">
      <svg class="contact__icon" viewBox="0 0 20 20" aria-hidden="true">
        <circle cx="10" cy="10" r="10" fill="var(--blue)"/>
        <path d="M6.5 5h2l1 2.5-1.3 1a6 6 0 0 0 3.3 3.3l1-1.3 2.5 1v2a1 1 0 0 1-1 1A9 9 0 0 1 5.5 6a1 1 0 0 1 1-1z" fill="#fff"/>
      </svg>
      <span>407-552-9031</span>
    </li>
    <li class="contact__item">
      <svg class="contact__icon" viewBox="0 0 20 20" aria-hidden="true">
        <rect x="1" y="4" width="18" height="12" rx="1.5" fill="var(--blue)"/>
        <path d="M2 5l8 6 8-6" fill="none" stroke="#fff" stroke-width="1.5"/>
      </svg>
      <span>brent@calderafilm.tv</span>
    </li>
    <li class="contact__item">
      <svg class="contact__icon" viewBox="0 0 20 20" aria-hidden="true">
        <circle cx="10" cy="10" r="9" fill="var(--blue)"/>
        <g fill="none" stroke="#fff" stroke-width="1.2">
          <ellipse cx="10" cy="10" rx="4" ry="9"/>
          <path d="M1 10h18M2.5 5.5h15M2.5 14.5h15"/>
        </g>
      </svg>
      <span>www.calderafilm.tv</span>
    </li>
  </ul>

  <span class="band band--grey"></span>
  <span class="band band--blue"></span>
  <span class="band band--sky"></span>
</section>

<section class="card card--back">
  <div class="back-brand">
    <span class="back-brand__mark"></span>
    <span class="back-brand__name">Caldera Film Works</span>
  </div>
</section>

</body>
</html>
```